Beautiful Customer Appreciation Gift Box Need Eye Catching Brochure

I need a brochure to include with small sample gift boxes that I send or give to companies who do door to door marketing of businesses, company reps, real estate designers and large companies looking for a unique customer appreciation gifts.

The brochure needs to capture the size variations and the limitless options for their budget and customization needs.

They are gift boxes that can be filled with cookies for the drug rep making an impression for the doc - after cookies are gone, the gift remains

At christmas, we fill them with baked goods and provide to each office. Every year as i visit the offices, they have last years gift box out as a decoration.

realtors can use them as a welcome to your new home gift filled with a bottle of wine and their papers left on the kitchen counter

We have had them used for baby shower gifts, kept later as a decoration.

that's the concept, i need it captured.
Marlow's Festive Nook is the current name
a tag line we came up with is It's all in the WRAPPINGS.
Updates

Project Deadline Extended
Reason: We are very close, I have my photoshoot tomorrow and I'd like to see and continue to tweek the current designs. I have pretty well deleted the designs we are not considering at this point. The others all have components we love. So I need a little more time and some tweaking to decide for sure.

Target Market(s)

the target is the company or individuals looking for gift giving options for clients and customers. From the door to door salesperson looking to make a splash or big impression to the large company looking for nice corporate gift ideas.

The concept of say goodbye to plain jane gift boxes that all look alike... Say goodbye to expensive gift wrap and bows that get thrown away in minutes.... and hello to a beautiful custom made gift box that will remain a decoration or keepsake box forever....

Industry/Entity Type

Retail

Font styles to use
Sans Serif
Script

Requirements
Must have
• IMPORTANT... I CAN and AM GETTING better pictures for the printing purposes. I'm looking more for the concept of the brochuure and layout design.
• I'd love to have it have some place holders for various pictures and descriptions - because each industry targets different people, I'd like to be able to change the front cover of the brochure with a picture of a box that targets that audience a little.
• For a real estate person... i might choose a beautiful centerpiece looking one... vs, the ob/gyn office, I might choose a baby one.
• I have some design skill, just 0 times and the programs have changed alot over the years, so this may go on to future work and a long design relationship as the company grows and changes. I do know photoshop and pagemaker from long ago so I should be able to drop in pics and text options. if we use compatible programs.
Nice to have
• would love to have some kind of background for the page - not just plain white background.
• i like angles and curves
Should not have
• boxy look.

```html
<!DOCTYPE html>
<html lang="en">
<head>
<meta charset="UTF-8">
<title>Gift Box Collection</title>
<link rel="stylesheet" href="https://fonts.googleapis.com/css2?family=Parisienne&family=Arimo&family=Tinos&display=swap">
<style>
  :root {
    --backdrop: #d5d6d8;
    --page: #3c4433;
    --page-deep: #343b2c;
    --line: #f4f3ee;
    --title: #ece8dc;
    --body: #f5f5f2;
    --frame: #ffffff;
  }
  * { margin: 0; padding: 0; box-sizing: border-box; }
  html, body { width: 1200px; height: 1000px; overflow: hidden; }
  body { background: var(--backdrop); position: relative; }

  .brochure-page {
    position: absolute; left: 103px; top: 116px; width: 993px; height: 767px;
    background: radial-gradient(ellipse at center, var(--page) 0%, var(--page-deep) 100%);
    box-shadow: 0 2px 6px rgba(0,0,0,0.25);
  }

  .rule { position: absolute; left: 130px; width: 938px; height: 2px; background: var(--line); }
  .rule--top { top: 176px; }
  .rule--bottom { top: 821px; }

  .flourish {
    position: absolute; left: 541px; width: 116px; height: 34px;
    background: var(--page); border-radius: 17px;
  }
  .flourish::after {
    content: ""; position: absolute; left: 8px; right: 8px; top: 12px; height: 10px;
    border-radius: 5px;
    background: linear-gradient(90deg, rgba(244,243,238,0.2), rgba(244,243,238,0.85), rgba(244,243,238,0.2));
  }
  .flourish--top { top: 150px; }
  .flourish--bottom { top: 815px; }

  .photo { position: absolute; width: 222px; height: 143px; border: 2px solid var(--frame); }
  .photo--letters { background: linear-gradient(90deg, #c9b8c4 0%, #d96fa6 30%, #e7cde0 60%, #d9c6b0 100%); }
  .photo--chest { background: linear-gradient(90deg, #6b5a3e 0%, #6f8a3b 35%, #7b6244 60%, #4a6a2c 80%, #c9b48a 100%); }
  .photo--fleurettes { background: linear-gradient(90deg, #7a5a48 0%, #e2a9b8 35%, #e8b9c8 60%, #d49aaa 100%); }
  .photo--lilas { background: linear-gradient(90deg, #6a5540 0%, #6a58a8 35%, #8a7cb8 55%, #2f3468 75%, #b89a6a 100%); }

  .info { position: absolute; width: 225px; color: var(--body); }
  .info__title {
    font-family: "Parisienne", cursive; font-size: 20px; line-height: 26px;
    color: var(--title); white-space: nowrap;
  }
  .info__text {
    margin-top: 2px; padding-left: 9px;
    font-family: "Arimo", Arial, sans-serif; font-size: 15.5px; line-height: 18px;
    white-space: nowrap;
  }
  .info__price {
    margin-top: 13px; padding-left: 9px;
    font-family: "Tinos", "Times New Roman", serif; font-size: 15px;
    display: flex; align-items: center; gap: 5px; white-space: nowrap;
  }
  .stars { font-family: Arial, sans-serif; font-size: 27px; line-height: 26px; }
</style>
</head>
<body>
  <div class="brochure-page"></div>

  <div class="rule rule--top"></div>
  <div class="flourish flourish--top" role="img" aria-label="Decorative scroll flourish"></div>
  <div class="rule rule--bottom"></div>
  <div class="flourish flourish--bottom" role="img" aria-label="Decorative scroll flourish"></div>

  <!-- Left column -->
  <div class="photo photo--letters" style="left:130px;top:196px" role="img" aria-label="Baby keepsake gift box with pink flower arrangement and plush toy"></div>
  <div class="info" style="left:362px;top:215px">
    <div class="info__title">Little Letters</div>
    <div class="info__text">Lorem ipsum dolor sit amet.<br>Lorem ipsum dolor sit amet.</div>
    <div class="info__price">Price : <span class="stars">★☆☆☆☆</span></div>
  </div>

  <div class="info" style="left:131px;top:370px">
    <div class="info__title">Wander Chest</div>
    <div class="info__text">Lorem ipsum dolor sit amet.<br>Lorem ipsum dolor sit amet.</div>
    <div class="info__price">Price : <span class="stars">★★★★★</span></div>
  </div>
  <div class="photo photo--chest" style="left:350px;top:351px" role="img" aria-label="Book-style keepsake box with green floral arrangement"></div>

  <div class="photo photo--fleurettes" style="left:130px;top:506px" role="img" aria-label="Pink vintage gift box with peonies"></div>
  <div class="info" style="left:362px;top:525px">
    <div class="info__title">Maison Des Fleurettes</div>
    <div class="info__text">Lorem ipsum dolor sit amet.<br>Lorem ipsum dolor sit amet.</div>
    <div class="info__price">Price : <span class="stars">★★★★★</span></div>
  </div>

  <div class="info" style="left:131px;top:680px">
    <div class="info__title">Le Salon De Lilas</div>
    <div class="info__text">Lorem ipsum dolor sit amet.<br>Lorem ipsum dolor sit amet.</div>
    <div class="info__price">Price : <span class="stars">★★★★☆</span></div>
  </div>
  <div class="photo photo--lilas" style="left:350px;top:661px" role="img" aria-label="Book box with purple pansy arrangement"></div>

  <!-- Right column -->
  <div class="photo photo--letters" style="left:627px;top:196px" role="img" aria-label="Baby keepsake gift box with pink flower arrangement and plush toy"></div>
  <div class="info" style="left:859px;top:215px">
    <div class="info__title">Little Letters</div>
    <div class="info__text">Lorem ipsum dolor sit amet.<br>Lorem ipsum dolor sit amet.</div>
    <div class="info__price">Price : <span class="stars">★☆☆☆☆</span></div>
  </div>

  <div class="info" style="left:628px;top:370px">
    <div class="info__title">Wander Chest</div>
    <div class="info__text">Lorem ipsum dolor sit amet.<br>Lorem ipsum dolor sit amet.</div>
    <div class="info__price">Price : <span class="stars">★★★★★</span></div>
  </div>
  <div class="photo photo--chest" style="left:847px;top:351px" role="img" aria-label="Book-style keepsake box with green floral arrangement"></div>

  <div class="photo photo--fleurettes" style="left:627px;top:506px" role="img" aria-label="Pink vintage gift box with peonies"></div>
  <div class="info" style="left:859px;top:525px">
    <div class="info__title">Maison Des Fleurettes</div>
    <div class="info__text">Lorem ipsum dolor sit amet.<br>Lorem ipsum dolor sit amet.</div>
    <div class="info__price">Price : <span class="stars">★★★★★</span></div>
  </div>

  <div class="info" style="left:628px;top:680px">
    <div class="info__title">Le Salon De Lilas</div>
    <div class="info__text">Lorem ipsum dolor sit amet.<br>Lorem ipsum dolor sit amet.</div>
    <div class="info__price">Price : <span class="stars">★★★★☆</span></div>
  </div>
  <div class="photo photo--lilas" style="left:847px;top:661px" role="img" aria-label="Book box with purple pansy arrangement"></div>
</body>
</html>
```